Web design for a Senior Home Care company

I want a web design for a home care company called Larkmoor Home Care. What LHC does is send caregivers into people's homes to assist with daily living needs such as companionship, food preparation, cleaning, bathing, using the bathroom, etc. Most of the clients are seniors. The people deciding to use LHC are usually the 50 year old children of these senior citizens. Most visitors to the site will be women searching for this service for their parents.

The call to action is to inspire the website visitors to call us to set up an appointment to meet them in their home. The site design should inspire confidence in Larkmoor Home Care to care for people's needs. We want to show the same attributes that a parent should have. Safety, Security and Loving Care.

Again, the goal of the site is to inspire and make it EASY for visitors to contact us either by phone call or through the website. The first choice is that they call us.

To help you with your ideas, In the attachments I've included different versions of our logo, a site map, examples of photos we might use and very rough draft of the website copy.

Target Market(s)

The customers will mostly be seniors. But, the people who will decide to use the company will the the 50 year old children of those seniors. Also, it is mostly women who are looking for help for their parents.

Industry/Entity Type

It Company

Number of Pages Required

5+ page

Requirements
Nice to have
• I want site visitors to easily be able to contact us with a phone call or through the website. The home page should inspire people to call us.

```html
<!DOCTYPE html>
<html lang="en">
<head>
<meta charset="utf-8">
<title>Larkmoor Home Care</title>
<link href="https://fonts.googleapis.com/css2?family=Montserrat:wght@300;400;500;600;700&family=Open+Sans:wght@400;600;700&family=Great+Vibes&display=swap" rel="stylesheet">
<style>
:root{
  --blue:#1f8fd6;
  --blue-dark:#0f6db5;
  --blue-deep:#0a5ea3;
  --sky:#4db3ec;
  --sky-light:#7ccaf2;
  --ink:#2c3440;
  --grey:#6c7480;
  --pale:#eef4f9;
  --white:#ffffff;
  --skin:#e9cdbb;
  --cream:#f4ece4;
}
*{margin:0;padding:0;box-sizing:border-box}
html,body{width:1200px;height:3711px;overflow:hidden}
body{font-family:"Open Sans",Arial,sans-serif;color:var(--ink);background:var(--white);position:relative}
.section{position:absolute;left:0;width:1200px;overflow:hidden}
.script{font-family:"Great Vibes",cursive;font-weight:400}
.abs{position:absolute}
.center{text-align:center;left:0;width:100%}

/* header */
.site-header{top:0;height:104px;background:var(--white)}
.brand{left:82px;top:18px;display:flex;align-items:center;gap:14px}
.brand-dot{width:54px;height:54px;border-radius:50%;background:var(--blue)}
.brand-name{font-family:"Montserrat",sans-serif;font-weight:700;color:var(--blue-dark);font-size:30px;line-height:1.05;letter-spacing:1px}
.call-box{left:861px;top:20px;width:260px;height:67px;border:2px solid #d9dde2;border-radius:6px;display:flex;align-items:center;gap:12px;padding-left:20px;background:#f7f8fa}
.call-box small{display:block;font-family:"Montserrat",sans-serif;font-size:12px;color:var(--grey);font-weight:600}
.call-box strong{display:block;font-family:"Montserrat",sans-serif;font-size:26px;color:var(--blue-dark);font-weight:600;line-height:1.1}

/* nav */
.main-nav{top:104px;height:62px;background:linear-gradient(var(--sky),var(--blue))}
.main-nav ul{list-style:none;display:flex;height:100%;padding-left:82px}
.main-nav li{font-family:"Montserrat",sans-serif;font-size:15px;font-weight:500;color:var(--white);display:flex;align-items:center;padding:0 22px}
.main-nav li.active{background:var(--blue-dark)}

/* hero */
.hero{top:166px;height:514px;background:
  radial-gradient(ellipse 30% 55% at 30% 35%,#f1e6dc 0%,rgba(241,230,220,0) 100%),
  radial-gradient(ellipse 28% 50% at 72% 40%,#e9c9b8 0%,rgba(233,201,184,0) 100%),
  radial-gradient(ellipse 40% 40% at 25% 95%,#8fb3d6 0%,rgba(143,179,214,0) 100%),
  linear-gradient(100deg,#d8c8bb 0%,#eadcd0 45%,#e2cbbd 70%,#cdb6a8 100%)}
.hero-shade{inset:0;background:rgba(30,45,70,.22)}
.hero h1{top:140px;font-size:60px;color:var(--white);text-shadow:0 2px 6px rgba(0,0,0,.2)}
.hero p{top:225px;left:240px;width:720px;font-family:"Montserrat",sans-serif;font-size:19px;color:var(--white);text-align:center;line-height:1.4}
.btn-solid{background:var(--blue);color:var(--white);font-family:"Montserrat",sans-serif;font-weight:600;font-size:16px;display:flex;align-items:center;justify-content:center;border-radius:3px}
.hero .btn-solid{left:465px;top:307px;width:270px;height:52px}
.hero-curve{left:0;bottom:-1px;width:1200px;height:110px}

/* welcome */
.welcome{top:680px;height:360px}
.welcome .script{top:40px;font-size:34px;color:var(--ink)}
.welcome h2{top:82px;font-family:"Montserrat",sans-serif;font-size:40px;font-weight:700;color:var(--blue-dark);letter-spacing:1px}
.welcome p{top:146px;left:140px;width:920px;text-align:center;font-size:14px;line-height:1.75;color:var(--grey)}
.btn-outline{border:2px solid var(--blue);color:var(--blue);font-family:"Montserrat",sans-serif;font-size:16px;font-weight:500;display:flex;align-items:center;justify-content:center}
.welcome .btn-outline{left:517px;top:260px;width:166px;height:48px}

/* steps */
.steps{top:1040px;height:440px;background:
  radial-gradient(ellipse 35% 60% at 55% 70%,rgba(255,255,255,.18),rgba(255,255,255,0)),
  linear-gradient(135deg,var(--sky-light),var(--blue) 60%,var(--blue-dark))}
.steps .script{top:52px;font-size:34px;color:var(--white)}
.steps h2{top:88px;font-family:"Montserrat",sans-serif;font-size:38px;font-weight:400;color:var(--white);letter-spacing:1px}
.step{width:330px;text-align:center;color:var(--white)}
.step-icon{width:110px;height:110px;margin:0 auto;border:3px solid var(--white);border-radius:50%;position:relative;display:flex;align-items:center;justify-content:center}
.step-num{position:absolute;top:-10px;left:-6px;width:32px;height:32px;border-radius:50%;background:var(--white);color:var(--blue);font-family:"Montserrat",sans-serif;font-weight:700;font-size:16px;display:flex;align-items:center;justify-content:center}
.step h3{font-family:"Montserrat",sans-serif;font-size:24px;font-weight:600;margin-top:18px}
.step p{font-size:13px;font-weight:600;line-height:1.6;margin-top:12px}

/* services */
.services{top:1480px;height:760px}
.services .script{top:58px;font-size:32px;color:var(--ink)}
.services h2{top:90px;font-family:"Montserrat",sans-serif;font-size:40px;font-weight:500;color:var(--blue-dark);letter-spacing:1px}
.services p{top:152px;left:160px;width:880px;text-align:center;font-size:14px;line-height:1.75;color:var(--grey)}
.services h4{top:240px;font-family:"Montserrat",sans-serif;font-size:20px;font-weight:600;color:var(--blue-dark)}
.orbit{left:421px;top:420px;width:360px;height:360px;border-radius:50%;background:radial-gradient(#fafbfc 40%,#eef1f4 100%)}
.care-photo{width:152px;height:152px;border-radius:50%;border:6px solid var(--blue);box-shadow:0 4px 10px rgba(0,0,0,.15)}
.care-photo.p1{background:radial-gradient(circle at 40% 40%,var(--skin),#c9b3a6 55%,#8fb0cf)}
.care-photo.p2{background:radial-gradient(circle at 60% 45%,var(--cream),#e4cfc2 50%,#b8c8d8)}
.care-photo.p3{background:radial-gradient(circle at 45% 50%,#efe0d4,#d8b9a6 55%,#9fb9cf)}
.care-photo.p4{background:radial-gradient(circle at 55% 40%,#e9e4e0,#b9b1ad 55%,#6f88a3)}
.care-photo.feature{background:var(--white);display:flex;align-items:center;justify-content:center;font-family:"Montserrat",sans-serif;font-weight:600;font-size:18px;text-align:center;line-height:1.2}
.core-name{left:451px;top:560px;width:300px;text-align:center;font-family:"Montserrat",sans-serif;font-weight:700;font-size:30px;color:var(--blue-dark)}

/* testimonials */
.testimonials{top:2240px;height:450px;background:
  repeating-linear-gradient(90deg,rgba(255,255,255,.04) 0 60px,rgba(0,0,0,.04) 60px 120px),
  linear-gradient(160deg,#2f86c8,#1d6fb3 50%,#2a7fc2)}
.testimonials h2{top:52px;font-family:"Montserrat",sans-serif;font-size:40px;font-weight:300;color:var(--white);letter-spacing:1px}
.testimonials h2 b{font-weight:700}
.quote{width:300px;text-align:center;color:var(--white)}
.avatar{width:100px;height:100px;margin:0 auto;border-radius:50%;border:5px solid var(--white);background:radial-gradient(circle at 50% 40%,var(--skin),#d5b9a8 45%,#e9eef3 75%)}
.quote p{font-size:14px;line-height:1.85;margin-top:30px}
.quote h3{font-family:"Montserrat",sans-serif;font-size:20px;font-weight:600;margin-top:20px}
.slide-arrow{top:205px;width:46px;height:46px;border-radius:50%;border:2px solid rgba(255,255,255,.7);display:flex;align-items:center;justify-content:center}

/* area */
.area{top:2690px;height:415px;background:var(--pale)}
.area-photo{left:0;top:0;width:640px;height:415px;background:
  radial-gradient(ellipse 30% 45% at 32% 55%,#3f86c4 0%,rgba(63,134,196,0) 100%),
  radial-gradient(ellipse 28% 40% at 55% 45%,#efe2d8 0%,rgba(239,226,216,0) 100%),
  linear-gradient(90deg,#f3ead8 0%,#f6f1ea 50%,var(--pale) 100%)}
.area .script{left:680px;top:88px;width:450px;text-align:center;font-size:44px;color:var(--ink)}
.area p{left:680px;top:152px;width:450px;text-align:center;font-size:15px;line-height:1.6;color:var(--grey)}
.zip-form{left:680px;top:254px;width:421px;height:57px;display:flex;border:3px solid var(--blue);background:var(--white)}
.zip-form span{display:flex;align-items:center;font-size:13px;color:var(--grey);padding:0 18px}
.zip-form .zip{flex:1;border-right:1px solid #d4d8dd}
.zip-form .sel{width:120px}
.zip-form .go{width:86px;background:var(--blue);color:var(--white);font-family:"Montserrat",sans-serif;font-weight:600;font-size:20px;justify-content:center;padding:0}

/* consult */
.consult{top:3105px;height:310px;background:linear-gradient(var(--sky),var(--blue))}
.consult .script{top:50px;font-size:50px;color:var(--white)}
.consult p{left:240px;top:122px;width:720px;text-align:center;font-size:15px;line-height:1.6;color:var(--white)}
.consult .btn-solid{left:495px;top:190px;width:210px;height:48px;background:var(--blue-deep)}
.glow{border-radius:50%}
.illus-left{left:90px;top:170px;width:200px;height:170px;background:radial-gradient(closest-side,rgba(255,255,255,.22),rgba(255,255,255,0))}
.illus-right{left:800px;top:140px;width:340px;height:210px;background:radial-gradient(closest-side,rgba(255,255,255,.22),rgba(255,255,255,0))}
.illus-mid{left:420px;top:250px;width:360px;height:100px;background:radial-gradient(closest-side,rgba(255,255,255,.18),rgba(255,255,255,0))}
.consult-wave{left:0;bottom:-1px;width:1200px;height:40px}

/* footer */
.site-footer{top:3415px;height:227px;background:var(--blue-dark)}
.site-footer h5{font-family:"Montserrat",sans-serif;font-size:22px;font-weight:500;color:var(--white);letter-spacing:1px}
.footer-col{top:22px;color:var(--white)}
.footer-col ul{list-style:none;margin-top:20px}
.footer-col li{font-size:13px;line-height:30px}
.divider{top:22px;width:1px;height:185px;background:rgba(255,255,255,.3)}
.contact-row{display:flex;gap:14px;font-size:13px;line-height:1.45;margin-top:14px}
.contact-row svg{flex:none;margin-top:2px}
.badge{width:80px;height:80px;border-radius:50%;background:radial-gradient(circle at 45% 40%,#f1f4f7,#a9b4bf);margin-top:14px}
.footer-name{left:890px;top:80px;width:200px;text-align:center;font-family:"Montserrat",sans-serif;font-weight:700;font-size:26px;color:rgba(255,255,255,.4)}
.copyright{top:3642px;height:69px;background:#0b4f8c;color:var(--white);font-size:13px;display:flex;align-items:center;justify-content:center;font-family:"Montserrat",sans-serif}
.copyright b{color:var(--sky-light);font-weight:600;margin-right:6px}
</style>
</head>
<body>

<header class="section site-header">
  <div class="abs brand"><span class="brand-dot"></span><span class="brand-name">LARKMOOR<br>HOME CARE</span></div>
  <div class="abs call-box">
    <svg width="34" height="34" viewBox="0 0 24 24"><path d="M6.6 10.8a15 15 0 0 0 6.6 6.6l2.2-2.2a1 1 0 0 1 1-.25 11.4 11.4 0 0 0 3.6.6 1 1 0 0 1 1 1V20a1 1 0 0 1-1 1A17 17 0 0 1 3 4a1 1 0 0 1 1-1h3.5a1 1 0 0 1 1 1c0 1.25.2 2.45.6 3.6a1 1 0 0 1-.25 1z" fill="#0f6db5"/></svg>
    <div><small>24/7 CALL US ON</small><strong>555.0142.870</strong></div>
  </div>
</header>

<nav class="section main-nav">
  <ul>
    <li class="active">HOME</li><li>ABOUT</li><li>SERVICES</li><li>FREE IN-HOME CONSULTATION</li><li>EMPLOYMENT</li><li>NEWS</li><li>CLIENT PORTAL</li>
  </ul>
</nav>

<section class="section hero" role="img" aria-label="Photo of a young caregiver smiling with a senior woman at home">
  <div class="abs hero-shade"></div>
  <h1 class="abs center script">Let's Enrich the lives of Seniors with Kindness &amp; Joy!</h1>
  <p class="abs">LARKMOOR HOME CARE offers an individualized approach to keep seniors safe &amp; sound at home, instead of anywhere else.</p>
  <div class="abs btn-solid">MAKE AN APPOINTMENT</div>
  <svg class="abs hero-curve" viewBox="0 0 1200 110" preserveAspectRatio="none">
    <path d="M0 20 Q600 140 1200 20 L1200 110 L0 110Z" fill="#1f8fd6"/>
    <path d="M0 32 Q600 152 1200 32 L1200 110 L0 110Z" fill="#fff"/>
  </svg>
</section>

<section class="section welcome">
  <div class="abs center script">Welcome to</div>
  <h2 class="abs center">LARKMOOR HOME CARE</h2>
  <p class="abs">Larkmoor Home Care is a local family owned and operated agency devoted to helping families like yours in the Inland Empire. We take pride in the relationships we develop with our clients. We understand this is a challenging time and we are dedicated to providing the peace of mind you deserve. At Larkmoor Home Care we do more than just watch your loved ones. We care for them with programs designed to keep them both mentally and physically comfortable, happy and healthy.</p>
  <div class="abs btn-outline">READ MORE</div>
</section>

<section class="section steps">
  <div class="abs center script">Step by Step</div>
  <h2 class="abs center">HOW TO GET STARTED ?</h2>
  <svg class="abs" style="left:0;top:0" width="1200" height="440">
    <path d="M330 170 Q430 120 530 180" stroke="#fff" stroke-width="3" fill="none"/>
    <path d="M518 170 L532 181 L516 188" stroke="#fff" stroke-width="3" fill="none"/>
    <path d="M670 180 Q770 120 860 165" stroke="#fff" stroke-width="3" stroke-dasharray="4 6" fill="none"/>
    <path d="M848 154 L862 166 L846 172" stroke="#fff" stroke-width="3" fill="none"/>
  </svg>
  <div class="abs step" style="left:82px;top:117px">
    <div class="step-icon"><span class="step-num">1</span>
      <svg width="50" height="50" viewBox="0 0 24 24" fill="none" stroke="#fff" stroke-width="1.6"><rect x="4" y="5" width="16" height="15" rx="2"/><path d="M4 10h16M8 3v4M16 3v4"/></svg></div>
    <h3>APPOINT</h3>
    <p>Lorem Ipsum is simply dummy text of the printing<br>and typesetting industry.</p>
  </div>
  <div class="abs step" style="left:429px;top:167px">
    <div class="step-icon"><span class="step-num">2</span>
      <svg width="50" height="50" viewBox="0 0 24 24" fill="none" stroke="#fff" stroke-width="1.6"><path d="M12 20s-7-4.5-7-10a4 4 0 0 1 7-2.6A4 4 0 0 1 19 10c0 5.5-7 10-7 10z"/></svg></div>
    <h3>24/7 CARE</h3>
    <p>Lorem Ipsum is simply dummy text of the printing<br>and typesetting industry.</p>
  </div>
  <div class="abs step" style="left:755px;top:117px">
    <div class="step-icon"><span class="step-num">3</span>
      <svg width="50" height="50" viewBox="0 0 24 24" fill="none" stroke="#fff" stroke-width="1.6"><path d="M4 11l8-7 8 7v9H4z"/><path d="M9 14l2 2 4-4"/></svg></div>
    <h3>ENJOY</h3>
    <p>Lorem Ipsum is simply dummy text of the printing<br>and typesetting industry.</p>
  </div>
</section>

<section class="section services">
  <div class="abs center script">Services We Offer</div>
  <h2 class="abs center">PROFESSIONAL.FAIR.SIMPLE.TRANSPARENT</h2>
  <p class="abs">Larkmoor Home Care offers a wide variety of home care services, from once a week visits to 24-hour care. Since every situation is unique, we work together with you to create the perfect program. Here is just a short list of the services we provide. Don't worry about pricing or deciphering a confusing invoice. All of these services are included in our simple One Flat Rate price structure.</p>
  <h4 class="abs center">Dementia &amp; Alzheimer's Care</h4>
  <div class="abs orbit"></div>
  <div class="abs core-name">LARKMOOR<br>HOME CARE</div>
  <div class="abs care-photo feature" style="left:525px;top:275px">Alzheimer's<br>Care</div>
  <div class="abs care-photo p1" style="left:312px;top:297px" role="img" aria-label="Photo of a caregiver helping a senior at a table"></div>
  <div class="abs care-photo p2" style="left:730px;top:297px" role="img" aria-label="Photo of a caregiver assisting a senior in bed"></div>
  <div class="abs care-photo p3" style="left:233px;top:544px" role="img" aria-label="Photo of a senior woman and her caregiver smiling"></div>
  <div class="abs care-photo p4" style="left:815px;top:544px" role="img" aria-label="Photo of a senior in a wheelchair with a caregiver"></div>
</section>

<section class="section testimonials" aria-label="Client testimonials">
  <h2 class="abs center">WHAT OUR <b>HAPPY CLIENTS</b> SAY</h2>
  <div class="abs slide-arrow" style="left:14px"><svg width="16" height="16" viewBox="0 0 16 16"><path d="M11 2 5 8l6 6" stroke="#fff" stroke-width="2" fill="none"/></svg></div>
  <div class="abs slide-arrow" style="left:1140px"><svg width="16" height="16" viewBox="0 0 16 16"><path d="M5 2l6 6-6 6" stroke="#fff" stroke-width="2" fill="none"/></svg></div>
  <div class="abs quote" style="left:97px;top:122px"><div class="avatar" role="img" aria-label="Client portrait"></div><p>"Lorem Ipsum is simply dummy text of the printing and typesetting industry. Lorem Ipsum has been the industry's standard dummy text ever since the 1500s."</p><h3>DEAN HARLOW</h3></div>
  <div class="abs quote" style="left:451px;top:122px"><div class="avatar" role="img" aria-label="Client portrait"></div><p>"Lorem Ipsum is simply dummy text of the printing and typesetting industry. Lorem Ipsum has been the industry's standard dummy text ever since the 1500s."</p><h3>NORA PELLIN</h3></div>
  <div class="abs quote" style="left:803px;top:122px"><div class="avatar" role="img" aria-label="Client portrait"></div><p>"Lorem Ipsum is simply dummy text of the printing and typesetting industry. Lorem Ipsum has been the industry's standard dummy text ever since the 1500s."</p><h3>TESS MARLOW</h3></div>
</section>

<section class="section area">
  <div class="abs area-photo" role="img" aria-label="Photo of a caregiver hugging a smiling senior woman"></div>
  <div class="abs script">Time to Enjoy Older Age</div>
  <p class="abs">Serving the Inland Empire and all other inland communities.<br>Check Out we Serve at your Area.</p>
  <div class="abs zip-form"><span class="zip">Enter Postal Code</span><span class="sel">Community ▾</span><span class="go">GO</span></div>
</section>

<section class="section consult">
  <div class="abs glow illus-left" role="img" aria-label="Line illustration of a house with a heart"></div>
  <div class="abs glow illus-mid" role="img" aria-label="Illustration of a row of raised hands"></div>
  <div class="abs glow illus-right" role="img" aria-label="Line illustration of an elderly couple"></div>
  <div class="abs center script">Free In-Home Consulting</div>
  <p class="abs">Lorem Ipsum is simply dummy text of the printing and typesetting industry. Lorem Ipsum has been the industry's standard dummy text ever since the 1500s.</p>
  <div class="abs btn-solid">CONTACT US NOW</div>
  <svg class="abs consult-wave" viewBox="0 0 1200 40" preserveAspectRatio="none">
    <path d="M0 25 Q300 5 600 20 T1200 15 L1200 40 L0 40Z" fill="#0f6db5"/>
  </svg>
</section>

<footer class="section site-footer">
  <div class="abs footer-col" style="left:82px"><h5>QUICK LINKS</h5>
    <ul><li>About</li><li>News</li><li>Privacy Policy</li><li>Terms &amp; Conditions</li></ul></div>
  <div class="abs divider" style="left:334px"></div>
  <div class="abs footer-col" style="left:359px"><h5>CONTACT US</h5>
    <div class="contact-row" style="margin-top:20px"><svg width="16" height="18" viewBox="0 0 24 24"><path d="M12 2a7 7 0 0 0-7 7c0 5 7 13 7 13s7-8 7-13a7 7 0 0 0-7-7zm0 9.5A2.5 2.5 0 1 1 12 6.5a2.5 2.5 0 0 1 0 5z" fill="#fff"/></svg><div><b>LARKMOOR HOME CARE</b><br>123 House name, Street,<br>City, Country - Zipcode</div></div>
    <div class="contact-row"><svg width="16" height="16" viewBox="0 0 24 24"><path d="M6.6 10.8a15 15 0 0 0 6.6 6.6l2.2-2.2a1 1 0 0 1 1-.25 11.4 11.4 0 0 0 3.6.6 1 1 0 0 1 1 1V20a1 1 0 0 1-1 1A17 17 0 0 1 3 4a1 1 0 0 1 1-1h3.5a1 1 0 0 1 1 1c0 1.25.2 2.45.6 3.6a1 1 0 0 1-.25 1z" fill="#fff"/></svg><div>(555) 0142 870</div></div>
    <div class="contact-row"><svg width="16" height="14" viewBox="0 0 24 18"><rect x="1" y="1" width="22" height="16" rx="2" fill="none" stroke="#fff" stroke-width="2"/><path d="M1 2l11 8 11-8" fill="none" stroke="#fff" stroke-width="2"/></svg><div>info@larkmoorhomecare.com</div></div>
  </div>
  <div class="abs divider" style="left:599px"></div>
  <div class="abs footer-col" style="left:623px"><h5>EXPERIENCE</h5>
    <div class="badge" role="img" aria-label="Experience badge"></div>
    <ul style="margin-top:8px"><li style="line-height:1.5">Proudly serving the clients in<br>need for over 30 years</li></ul></div>
  <div class="abs footer-name">LARKMOOR<br>HOME CARE</div>
</footer>

<div class="section copyright"><b>© LARKMOOR HOME CARE</b> - 2016. All Rights Reserved</div>

</body>
</html>
```